Menu for Coffee Shop / Restaurant

we are looking for someone to redesign our menus. would like something clean and modern, not too over the top. The business is a coffee shop during the day and transitions to a bar/restaurant in the evenings, so we need a design versatile enough to be used on everything from breakfast menus to cocktail menus. i've attached logo files as well as the current menu files. We're looking to do one menu each for breakfast, brunch (served only on weekends), one that combines the items listed on the attached lunch and dinner menus, and a dessert menu.

Industry/Entity Type

Business

Colors

Designer to choose colors to be used in the design.

Requirements
Must have
• 4 menus : breakfast, brunch, regular food service (combine lunch and dinner menus) and a dessert menu
Nice to have
• would prefer that each menu fit on 1 page, not double sided. We're ok with using legal size paper in order to accomodate

```html
<!DOCTYPE html>
<html lang="en">
<head>
<meta charset="utf-8">
<title>Copperleaf Breakfast Menu</title>
<link rel="stylesheet" href="https://fonts.googleapis.com/css2?family=Josefin+Sans:wght@600;700&family=Open+Sans:wght@400;600;700&display=swap">
<style>
  :root {
    --wood-light: #f0c980;
    --wood: #e4af5c;
    --wood-dark: #cf9443;
    --brown: #4a2414;
    --orange: #eb8f45;
    --cream: #fbe5bf;
    --cyan: #32c2e2;
    --ink: #3b1f12;
    --paper: #ffffff;
  }
  * { box-sizing: border-box; margin: 0; padding: 0; }
  html, body { width: 758px; height: 1200px; overflow: hidden; background: var(--paper); }
  body { font-family: "Open Sans", sans-serif; color: var(--ink); }

  .menu {
    position: relative;
    width: 758px; height: 1200px;
    display: flex; flex-direction: column;
    background: linear-gradient(180deg, var(--wood-light), var(--wood) 55%, var(--wood-dark));
    padding: 40px 48px 64px 64px;
  }
  .edge-rule { position: absolute; left: 28px; top: 0; bottom: 0; width: 6px; background: var(--cyan); }
  .bottom-rule { position: absolute; left: 0; right: 0; bottom: 26px; height: 8px; background: var(--cyan); }

  .masthead { display: flex; align-items: center; gap: 22px; margin-bottom: 26px; }
  .brand-dot { width: 100px; height: 100px; border-radius: 50%; background: var(--cream); flex: none; }
  .brand-name { font-family: "Josefin Sans", sans-serif; font-weight: 700; font-size: 48px; letter-spacing: 4px; color: var(--brown); line-height: 1; }
  .menu-title { font-family: "Josefin Sans", sans-serif; font-weight: 700; font-size: 23px; letter-spacing: 6px; color: var(--orange); margin-top: 8px; }

  .section-head { font-family: "Josefin Sans", sans-serif; font-weight: 700; font-size: 28px; color: var(--brown); text-transform: uppercase; letter-spacing: 1px; line-height: 1.1; }
  .section-head small { font-family: "Open Sans", sans-serif; font-size: 15px; font-weight: 600; text-transform: none; letter-spacing: 0; margin-left: 12px; }

  .build { display: flex; gap: 28px; margin-top: 16px; }
  .build-list { flex: 1; font-size: 16px; line-height: 1.85; }
  .build-list .lead { font-weight: 700; }
  .sides { width: 270px; background: var(--cream); border: 3px solid var(--brown); padding: 16px 20px; font-size: 15px; align-self: flex-start; }
  .sides h3 { font-family: "Josefin Sans", sans-serif; font-size: 19px; color: var(--brown); margin-bottom: 8px; }
  .sides table { width: 100%; border-collapse: collapse; }
  .sides td { padding: 4px 0; border-bottom: 1px solid rgba(74,36,20,0.25); }
  .sides td.price { text-align: right; font-weight: 700; }

  .band { height: 12px; background: var(--brown); margin: 26px -48px 26px -30px; flex: none; }

  .panel { flex: 1; display: flex; flex-direction: column; padding: 24px 22px; margin: 0 -22px; }
  .panel.sandwiches { background: rgba(235,143,69,0.55); }
  .panel.omelets { background: rgba(251,229,191,0.7); margin-top: 22px; }

  .items { list-style: none; flex: 1; display: flex; flex-direction: column; justify-content: space-evenly; margin-top: 10px; }
  .item-name { font-weight: 700; font-size: 18px; text-transform: uppercase; color: var(--brown); }
  .item-price { font-weight: 700; font-size: 18px; color: var(--brown); margin-left: 10px; }
  .item-desc { font-size: 15px; line-height: 1.5; margin-top: 2px; }
</style>
</head>
<body>
<main class="menu">
  <div class="edge-rule"></div>

  <header class="masthead">
    <span class="brand-dot"></span>
    <div>
      <div class="brand-name">COPPERLEAF</div>
      <div class="menu-title">BREAKFAST</div>
    </div>
  </header>

  <section class="build-your-own">
    <h2 class="section-head">Build Your Own Breakfast</h2>
    <div class="build">
      <div class="build-list">
        <p class="lead">Choose any three items $8.95</p>
        <p>Two Eggs Any Style</p>
        <p>Applewood Bacon</p>
        <p>Pork Sausage Links</p>
        <p>Crispy Hash Browns</p>
        <p>Buttermilk Pancake</p>
        <p>Toast or English Muffin</p>
        <p>Seasonal Fresh Fruit</p>
      </div>
      <aside class="sides">
        <h3>Sides</h3>
        <table>
          <tr><td>One Egg</td><td class="price">$1.95</td></tr>
          <tr><td>Bacon</td><td class="price">$3.50</td></tr>
          <tr><td>Sausage</td><td class="price">$3.50</td></tr>
          <tr><td>Hash Browns</td><td class="price">$2.95</td></tr>
          <tr><td>Toast</td><td class="price">$1.95</td></tr>
          <tr><td>Fruit Cup</td><td class="price">$3.95</td></tr>
          <tr><td>Yogurt Parfait</td><td class="price">$4.50</td></tr>
        </table>
      </aside>
    </div>
  </section>

  <div class="band"></div>

  <section class="panel sandwiches">
    <h2 class="section-head">Sandwiches <small>served with hash browns or fruit</small></h2>
    <ul class="items">
      <li><span class="item-name">Egg &amp; Cheese</span><span class="item-price">$8.95</span>
        <p class="item-desc">Fried egg, cheddar and bacon on a toasted brioche bun.</p></li>
      <li><span class="item-name">Breakfast Burrito</span><span class="item-price">$9.95</span>
        <p class="item-desc">Scrambled eggs, chorizo, peppers, onions and salsa in a flour tortilla.</p></li>
      <li><span class="item-name">Breakfast Burger</span><span class="item-price">$11.95</span>
        <p class="item-desc">Beef patty, fried egg, bacon and cheddar on a toasted bun.</p></li>
    </ul>
  </section>

  <section class="panel omelets">
    <h2 class="section-head">Omelets <small>served with toast and hash browns</small></h2>
    <ul class="items">
      <li><span class="item-name">Egg White Omelet</span><span class="item-price">$9.95</span>
        <p class="item-desc">Egg whites, spinach, tomato and feta cheese.</p></li>
      <li><span class="item-name">Veggie Omelet</span><span class="item-price">$9.95</span>
        <p class="item-desc">Mushrooms, peppers, onions, tomato and cheddar.</p></li>
      <li><span class="item-name">Smoked Salmon Omelet</span><span class="item-price">$11.95</span>
        <p class="item-desc">Smoked salmon, cream cheese, capers and fresh dill.</p></li>
    </ul>
  </section>

  <div class="bottom-rule"></div>
</main>
</body>
</html>
```